Northridge Valley Arms Banner

We are looking for a banner ad that we will run on DawnPostly.com the size is 758x120 and also a matching one that is 300x250 can be animated or static.final graphics will need to be submitted in jpg, gif or similar format. Our shop is a firearms business called "Northridge Valley Arms" located at 412 Route 19 South, Pellham Ms. 38412 phone is 662-574-3108 . it need to be modern and eye catching and be more geared to the tactical side. Our website is
northridgevalarms.com the banners DO NOT have to match website. would like a DIFFERENT LOOK than my website

```html
<!DOCTYPE html>
<html lang="en">
<head>
<meta charset="utf-8">
<title>Northridge Valley Arms – Banner Set</title>
<link href="https://fonts.googleapis.com/css2?family=Lato:wght@400;700;900&display=swap" rel="stylesheet">
<style>
  :root{
    --stage:#3a3839;
    --navy:#0d3460;
    --slate:#232c27;
    --gold:#ffcc00;
    --ink:#0b0b0b;
    --sky:#4fb3e3;
    --white:#ffffff;
    --sand-light:#b99a6a;
    --sand-dark:#5e4326;
  }
  *{box-sizing:border-box;margin:0;padding:0}
  html,body{width:1200px;height:1000px;overflow:hidden;background:var(--stage);font-family:"Lato",sans-serif}
  .stage{position:relative;width:1200px;height:1000px}

  .banner{position:absolute;overflow:hidden;border:1px solid var(--white)}
  .banner svg.art{position:absolute;left:0;top:0}
  .theme-navy{--base:var(--navy)}
  .theme-slate{--base:var(--slate)}
  .base-fill{fill:var(--base)}

  .brand{position:absolute;display:flex;align-items:center;gap:8px}
  .brand__mark{width:38px;height:38px;border-radius:50%;background:var(--gold);flex:none}
  .brand__name{color:var(--gold);font-weight:900;font-size:17px;line-height:1.05}

  .headline{position:absolute;color:var(--ink);font-weight:900;text-align:center;line-height:.92;letter-spacing:-.3px;text-shadow:1px 1px 0 rgba(255,255,255,.55)}
  .offer{position:absolute;color:var(--ink);text-align:center;letter-spacing:1.1px}
  .offer b{font-weight:700}

  .contact{position:absolute;color:var(--white);font-weight:700;white-space:nowrap}
  .contact .label{color:var(--sky);letter-spacing:.8px}
  .contact .city{color:var(--sky);font-weight:700}
  .contact .url{letter-spacing:1px}

  /* square 300x250 format */
  .banner--square{width:338px;height:282px;top:195px}
  .banner--square .brand{left:8px;top:22px;width:190px}
  .banner--square .headline{left:0;top:91px;width:178px;font-size:28px}
  .banner--square .offer{left:8px;top:172px;width:175px;font-size:13.5px;line-height:18px}
  .banner--square .contact{left:5px;font-size:12.5px}
  .banner--square .row-1{top:240px}
  .banner--square .row-2{top:262px;font-size:12px}
  .banner--square .row-2 .small{font-size:9.5px}

  /* wide 758x120 format */
  .banner--wide{width:760px;height:122px;left:241px}
  .banner--wide .brand{left:10px;top:22px;width:200px}
  .banner--wide .headline{left:232px;top:4px;width:240px;font-size:29px}
  .banner--wide .offer{left:232px;top:56px;width:240px;font-size:13.5px;line-height:17px}
  .banner--wide .contact{top:99px;font-size:12.5px}
</style>
</head>
<body>
<main class="stage">

  <!-- Square, navy -->
  <section class="banner banner--square theme-navy" style="left:241px">
    <svg class="art" width="338" height="282" viewBox="0 0 338 282">
      <rect class="base-fill" width="338" height="282"/>
      <polygon points="0,92 100,84 112,72 124,82 200,68 200,232 0,232" fill="var(--gold)"/>
      <path d="M195 0 Q162 116 182 232 L338 232 L338 0 Z" fill="var(--white)"/>
      <defs><linearGradient id="sandA" x1="0" y1="0" x2="1" y2="1"><stop offset="0" stop-color="var(--sand-light)"/><stop offset="1" stop-color="var(--sand-dark)"/></linearGradient></defs>
      <path role="img" aria-label="Revolver and brass cartridges resting on gravel" d="M203 0 Q170 116 190 232 L338 232 L338 0 Z" fill="url(#sandA)"/>
      <rect class="base-fill" y="232" width="338" height="50"/>
    </svg>
    <div class="brand"><span class="brand__mark"></span><span class="brand__name">Northridge Valley Arms</span></div>
    <h2 class="headline">Guns,<br>Ammo &amp;<br>Accessories!</h2>
    <p class="offer">low cost firearm<br>transfers for only<br><b>$20.00</b> per firearm!</p>
    <p class="contact row-1"><span class="label">ADRESS:</span> 412 Route 19 South, / <span class="city">Pellham Ms. 38412</span></p>
    <p class="contact row-2"><span class="label">PHONE:</span> 662-574-3108 <span class="label small">WEB:</span> <span class="url small">northridgevalarms.com</span></p>
  </section>

  <!-- Square, slate -->
  <section class="banner banner--square theme-slate" style="left:620px">
    <svg class="art" width="338" height="282" viewBox="0 0 338 282">
      <rect class="base-fill" width="338" height="282"/>
      <polygon points="0,92 100,84 112,72 124,82 200,68 200,232 0,232" fill="var(--gold)"/>
      <path d="M195 0 Q162 116 182 232 L338 232 L338 0 Z" fill="var(--white)"/>
      <defs><linearGradient id="sandB" x1="0" y1="0" x2="1" y2="1"><stop offset="0" stop-color="var(--sand-light)"/><stop offset="1" stop-color="var(--sand-dark)"/></linearGradient></defs>
      <path role="img" aria-label="Revolver and brass cartridges resting on gravel" d="M203 0 Q170 116 190 232 L338 232 L338 0 Z" fill="url(#sandB)"/>
      <rect class="base-fill" y="232" width="338" height="50"/>
    </svg>
    <div class="brand"><span class="brand__mark"></span><span class="brand__name">Northridge Valley Arms</span></div>
    <h2 class="headline">Guns,<br>Ammo &amp;<br>Accessories!</h2>
    <p class="offer">low cost firearm<br>transfers for only<br><b>$20.00</b> per firearm!</p>
    <p class="contact row-1"><span class="label">ADRESS:</span> 412 Route 19 South, / <span class="city">Pellham Ms. 38412</span></p>
    <p class="contact row-2"><span class="label">PHONE:</span> 662-574-3108 <span class="label small">WEB:</span> <span class="url small">northridgevalarms.com</span></p>
  </section>

  <!-- Wide, navy -->
  <section class="banner banner--wide theme-navy" style="top:510px">
    <svg class="art" width="760" height="122" viewBox="0 0 760 122">
      <rect class="base-fill" width="760" height="122"/>
      <polygon points="234,0 480,0 480,92 220,92 225,56 216,48 229,40" fill="var(--gold)"/>
      <path d="M478 0 Q458 60 476 122 L760 122 L760 0 Z" fill="var(--white)"/>
      <defs><linearGradient id="sandC" x1="0" y1="0" x2="1" y2="1"><stop offset="0" stop-color="var(--sand-light)"/><stop offset="1" stop-color="var(--sand-dark)"/></linearGradient></defs>
      <path role="img" aria-label="Revolver and brass cartridges resting on gravel" d="M485 0 Q465 60 483 122 L760 122 L760 0 Z" fill="url(#sandC)"/>
      <path class="base-fill" d="M0 92 L748 92 Q742 108 736 122 L0 122 Z"/>
    </svg>
    <div class="brand"><span class="brand__mark"></span><span class="brand__name">Northridge Valley Arms</span></div>
    <h2 class="headline">Guns, Ammo &amp;<br>Accessories!</h2>
    <p class="offer">low cost firearm transfers for<br>only <b>$20.00</b> per firearm!</p>
    <p class="contact" style="left:8px"><span class="label">ADRESS:</span> 412 Route 19 South, / <span class="city">Pellham Ms. 38412</span></p>
    <p class="contact" style="left:352px"><span class="label">PHONE:</span> 662-574-3108</p>
    <p class="contact" style="left:531px"><span class="label">WEB:</span> <span class="url">northridgevalarms.com</span></p>
  </section>

  <!-- Wide, slate -->
  <section class="banner banner--wide theme-slate" style="top:652px">
    <svg class="art" width="760" height="122" viewBox="0 0 760 122">
      <rect class="base-fill" width="760" height="122"/>
      <polygon points="234,0 480,0 480,92 220,92 225,56 216,48 229,40" fill="var(--gold)"/>
      <path d="M478 0 Q458 60 476 122 L760 122 L760 0 Z" fill="var(--white)"/>
      <defs><linearGradient id="sandD" x1="0" y1="0" x2="1" y2="1"><stop offset="0" stop-color="var(--sand-light)"/><stop offset="1" stop-color="var(--sand-dark)"/></linearGradient></defs>
      <path role="img" aria-label="Revolver and brass cartridges resting on gravel" d="M485 0 Q465 60 483 122 L760 122 L760 0 Z" fill="url(#sandD)"/>
      <path class="base-fill" d="M0 92 L748 92 Q742 108 736 122 L0 122 Z"/>
    </svg>
    <div class="brand"><span class="brand__mark"></span><span class="brand__name">Northridge Valley Arms</span></div>
    <h2 class="headline">Guns, Ammo &amp;<br>Accessories!</h2>
    <p class="offer">low cost firearm transfers for<br>only <b>$20.00</b> per firearm!</p>
    <p class="contact" style="left:8px"><span class="label">ADRESS:</span> 412 Route 19 South, / <span class="city">Pellham Ms. 38412</span></p>
    <p class="contact" style="left:352px"><span class="label">PHONE:</span> 662-574-3108</p>
    <p class="contact" style="left:531px"><span class="label">WEB:</span> <span class="url">northridgevalarms.com</span></p>
  </section>

</main>
</body>
</html>
```